Business Card Design for TrailReady

TrailReady is an online e-commerce store specializing in Outdoors Gear such as camping equipment, hunting and shooting equipment, tactical gear and more. See complete line at trailready-gear.example
Logo: http://www.trailready-gear.example/media/ID/Ready.jpg
http://www.trailready-gear.example/media/ID/TrailReady-blue.jpg

Target Market(s)

20-40 Male

Industry/Entity Type

E-Commerce

```html
<!DOCTYPE html>
<html lang="en">
<head>
<meta charset="utf-8">
<title>TrailReady Business Card</title>
<link rel="stylesheet" href="https://fonts.googleapis.com/css2?family=Andada+Pro:wght@400;700&display=swap">
<style>
  :root {
    --stage: #dcdde3;
    --brand-blue: #1d4a80;
    --front-grey: #9ea3a7;
    --front-grey-light: #b3b7ba;
    --back-slate: #6d8399;
    --back-slate-dark: #56697e;
    --panel-white: #f4f5f6;
    --ink-blue: #1f3f6e;
    --white: #ffffff;
  }
  * { box-sizing: border-box; margin: 0; padding: 0; }
  html, body { width: 1200px; height: 900px; overflow: hidden; }
  body {
    background: var(--stage);
    position: relative;
    font-family: "Andada Pro", Georgia, serif;
  }
  .card {
    position: absolute;
    width: 560px;
    height: 320px;
    border-radius: 4px;
    overflow: hidden;
    box-shadow: 0 10px 26px rgba(40, 50, 70, 0.22);
  }

  /* Front */
  .card-front {
    left: 90px;
    top: 480px;
    background: radial-gradient(ellipse at 40% 40%, var(--front-grey-light), var(--front-grey));
  }
  .front-brand {
    position: absolute;
    inset: 0;
    display: flex;
    flex-direction: column;
    align-items: center;
    justify-content: center;
    color: var(--brand-blue);
  }
  .brand-row {
    display: flex;
    align-items: center;
    gap: 16px;
  }
  .brand-square {
    width: 30px;
    height: 30px;
    background: var(--brand-blue);
  }
  .brand-name {
    font-weight: 700;
    font-size: 54px;
    line-height: 1;
  }
  .front-tagline {
    font-weight: 400;
    font-size: 19px;
    margin-top: 14px;
  }

  /* Back */
  .card-back {
    left: 560px;
    top: 110px;
    background: linear-gradient(135deg, var(--back-slate) 0%, var(--back-slate-dark) 55%, var(--back-slate) 100%);
  }
  .back-decoration {
    position: absolute;
    inset: 0;
    background: radial-gradient(ellipse at 60% 45%, rgba(255,255,255,0.10), rgba(0,0,0,0.08));
  }
  .holder-name {
    position: absolute;
    top: 26px;
    left: 0; right: 0;
    text-align: center;
    font-weight: 700;
    font-size: 34px;
    color: var(--white);
  }
  .contact-panel {
    position: absolute;
    left: 34px;
    right: 24px;
    top: 82px;
    height: 176px;
    border-radius: 22px;
    background: var(--panel-white);
    color: var(--ink-blue);
    font-size: 19px;
    line-height: 1.2;
  }
  .holder-title {
    position: absolute;
    top: 10px;
    left: 0; right: 0;
    text-align: center;
  }
  .phones {
    position: absolute;
    left: 16px;
    top: 40px;
    display: grid;
    grid-template-columns: 72px auto;
    row-gap: 2px;
  }
  .address {
    position: absolute;
    right: 18px;
    top: 90px;
    text-align: right;
  }
  .email {
    position: absolute;
    left: 62px;
    top: 140px;
    font-size: 18px;
  }
  .web-address {
    position: absolute;
    left: 0; right: 0;
    bottom: 12px;
    text-align: center;
    color: var(--white);
    font-size: 24px;
    opacity: 0.9;
  }
</style>
</head>
<body>
  <section class="card card-back" aria-label="Card back">
    <div class="back-decoration" role="img" aria-label="Faint textured background in slate blue tones"></div>
    <h1 class="holder-name">Dorian Velk</h1>
    <div class="contact-panel">
      <p class="holder-title">Purchasing Manager</p>
      <dl class="phones">
        <dt>Cell:</dt><dd>555 014 2290</dd>
        <dt>Office:</dt><dd>555 014 7731</dd>
      </dl>
      <p class="address">PO BOX 208<br>Pinehollow, IL 60000</p>
      <p class="email">Purchasing@trailready-gear.example</p>
    </div>
    <p class="web-address">trailready-gear.example</p>
  </section>

  <section class="card card-front" aria-label="Card front">
    <div class="front-brand">
      <div class="brand-row">
        <span class="brand-square" aria-hidden="true"></span>
        <p class="brand-name">TrailReady</p>
      </div>
      <p class="front-tagline">Outdoor Gear for Every Trail</p>
    </div>
  </section>
</body>
</html>
```